Digital Medical Care Start-up: New Web Design Needed

We are a startup in Boston, USA. Our current website has mostly acceptable content but looks outdated and it is ineffective. Viewers - especially possible investors - are turned off. It may also have too much content - especially the table. Current site Https://CareLoomKits.com

Business: we produce apps for surgeons to give their patients. The apps describe the medical procedure they will have, how to prepare, what to do to speed recovery, and how to interpret any symptoms. One app for each medical procedure - there are over 200.

LIKES
https://www.kestrivamed.com/
https://www.fenworthclinix.com/en/
https://zorandi.com/about/
DISLIKES
https://plax-ora.com/
https://www.tundravita.com/
https://www.grelvin-clinic.net/
https://www.quessa.com/

Target Market(s)

Audience: Medical Surgeons (customers) and Investors (we will do our first capital raise afterward the new website) in USA.

Coding

Number of Pages Required

Font styles to use
Other font styles liked:
• Candara

Colors
0455a3
f37122

Requirements
Must have
• OUTPUT:
We want a fully Responsive Version.
We do not use Wordpress. The page layout (or template) should be html + css + images + a little JavaScript.
The first page is the landing page. The second page would be the template on which we put the remaining content.
After delivery, the html would be merged into the existing framework. The site needs to be built on a template so it can be managed by an average quasi-tech person, without the need for a coder.

See exisiting company and product logos. They will remain unchanged, so make sure the website is compatable with the current logos.
Nice to have
• We have attached an idea of ours. This is meant for your stimulation, not necessarily for replication. Our attachment does not have all the content details, but the outline is correct.

```html
<!DOCTYPE html>
<html lang="en">
<head>
<meta charset="utf-8">
<title>CareLoomKits – Procedure eCare</title>
<link href="https://fonts.googleapis.com/css2?family=Lato:wght@400;700;900&display=swap" rel="stylesheet">
<style>
:root{
  --blue:#0a7ce6;
  --brand:#0455a3;
  --navy:#0b2f5c;
  --orange:#f37122;
  --bg:#f7f9fd;
  --gray-bg:#f3f4f6;
  --testi-bg:#f4f6f9;
  --text:#2a2f3a;
  --muted:#6b7380;
  --line:#dde3ea;
  --footer:#0e0e10;
}
*{margin:0;padding:0;box-sizing:border-box}
html,body{width:1200px;height:4717px;overflow:hidden}
body{font-family:"Lato",sans-serif;color:var(--text);background:var(--bg)}
.page{position:relative;width:1200px;height:4717px;overflow:hidden}
.abs{position:absolute}
.dot{position:absolute;border-radius:50%;background:var(--orange)}

/* nav */
.logo{display:flex;align-items:center;gap:10px;font-weight:900;color:var(--brand);font-size:26px}
.logo-mark{width:40px;height:40px;border-radius:50%;background:var(--brand)}
.nav{left:487px;top:44px;display:flex;gap:34px;font-size:13px;color:var(--navy)}
.nav .active{font-weight:700;position:relative}
.nav .active:after{content:"";position:absolute;left:50%;top:24px;width:4px;height:4px;border-radius:50%;background:var(--navy)}
.btn{background:var(--blue);color:#fff;font-size:13px;display:flex;align-items:center;justify-content:center}
.nav-cta{left:948px;top:28px;width:152px;height:47px;border-radius:24px}

/* hero */
.hero-deco{left:1045px;top:84px;width:122px;height:119px;background:var(--blue);border-radius:14px}
.hero-photo{left:519px;top:110px;width:619px;height:563px;border-radius:18px;background:linear-gradient(135deg,#d9d3cb,#a89888 55%,#3d5a80)}
.eyebrow{left:100px;top:255px;font-size:36px;color:var(--navy);padding-left:12px;border-left:3px solid var(--orange);line-height:40px}
.hero-title{left:100px;top:335px;font-size:54px;font-weight:900;color:var(--navy);line-height:56px}
.hero-sub{left:100px;top:476px;font-size:19px;font-weight:700;color:var(--navy);line-height:36px}
.hero-cta{left:99px;top:588px;width:216px;height:50px;border-radius:3px;font-weight:700}

/* intro */
.intro{left:0;top:815px;width:1190px;text-align:center;font-size:37px;font-weight:700;color:var(--navy);line-height:54px}
.card{position:absolute;top:1010px;width:307px;height:335px;background:#fff;border-radius:10px;box-shadow:0 8px 30px rgba(20,50,100,.06);padding:32px 34px}
.card.featured{background:var(--blue);height:395px;color:#fff;box-shadow:0 16px 40px rgba(10,124,230,.3)}
.card h3{font-size:22px;color:var(--navy);margin:58px 0 14px;line-height:27px}
.card.featured h3{color:#fff;margin-top:64px}
.card p{font-size:12.5px;line-height:22.5px;color:#4a4f58;padding-right:16px}
.card.featured p{color:#e6f0fc}

/* benefits */
.benefits{left:0;top:1522px;width:1200px;height:758px;background:var(--gray-bg)}
.sec-title{text-align:center;font-weight:700;color:var(--navy)}
.benefits h2{position:absolute;left:0;top:55px;width:1180px;font-size:37px;line-height:54px}
.circle-photo{left:98px;top:1755px;width:444px;height:404px;border-radius:50%;background:radial-gradient(circle at 40% 45%,#8a9bb0,#4b5f78 60%,#2d3b4f);border:10px solid #fff;box-shadow:0 10px 30px rgba(0,0,0,.08)}
.sm-photo{border-radius:50%;border:6px solid #fff;background:linear-gradient(135deg,#d8cfc6,#6a4f3f)}
.acc{left:594px;width:506px;border-bottom:1px solid var(--line)}
.acc h4{font-size:21px;color:var(--navy);font-weight:700;display:flex;justify-content:space-between;align-items:center}
.acc h4 span{color:var(--orange);font-size:30px;font-weight:400}
.acc p{font-size:12.5px;line-height:22.5px;color:#4a4f58;margin-top:14px}

/* testimonials */
.testi-bg{left:0;top:2280px;width:1200px;height:740px;background:var(--testi-bg)}
.testi{left:157px;top:2380px;width:880px;height:550px;background:#fff}
.testi .bar{position:absolute;left:420px;top:50px;width:40px;height:3px;background:var(--orange)}
.testi h2{position:absolute;left:0;top:70px;width:860px;font-size:37px}
.quote{font-size:56px;font-weight:900;color:var(--navy);line-height:1}
.testi-text{left:552px;top:2570px;width:350px;font-size:13px;line-height:22.5px;color:#4a4f58}
.name{left:544px;top:2732px;font-size:24px;color:#6b6f78;font-weight:700}
.role{left:544px;top:2772px;font-size:12.5px;color:var(--muted);line-height:18px}
.arrow{width:46px;height:46px;border-radius:50%;display:flex;align-items:center;justify-content:center}
.pager{left:546px;top:2878px;width:100px;height:13px;border-radius:7px;background:var(--orange);display:flex;gap:6px;align-items:center;justify-content:center}
.pager i{width:4px;height:4px;border-radius:50%;background:#fff}
.pager i.on{width:8px;height:8px}

/* clinical groups */
.groups{left:0;top:3020px;width:1200px;height:525px;background:var(--gray-bg)}
.groups h2{position:absolute;top:65px;width:1210px;font-size:38px}
.group{position:absolute;width:281px;height:117px;background:#fff;padding:22px 16px}
.g-icon{position:absolute;left:16px;top:24px;width:38px;height:38px;background:var(--orange);border-radius:3px}
.g-body{margin-left:58px}
.g-body h5{font-size:19px;color:var(--navy);font-weight:700;margin-bottom:6px}
.g-body p{font-size:9.5px;line-height:16px;color:#3d4350}
.g-body b{color:var(--navy)}
.g-num{position:absolute;right:10px;top:10px;font-size:8px;color:#555}

/* newsletter */
.news{left:99px;top:3637px;width:1001px;height:400px;background:var(--blue);border-radius:16px;text-align:center;color:#fff}
.news h2{margin-top:50px;font-size:38px;font-weight:700}
.news p{font-size:13px;margin-top:10px}
.field{position:absolute;left:142px;top:181px;width:710px;height:97px;background:#fff;border-radius:4px;display:flex;align-items:center;padding:0 24px;justify-content:space-between}
.field span{font-size:14px;color:#2a2f3a}
.field .send{width:144px;height:60px;border-radius:2px;color:#fff;font-size:13px}

/* footer */
.footer{left:0;top:4140px;width:1200px;height:577px;background:var(--footer);color:#fff}
.f-logo{position:absolute;left:0;top:93px;width:1200px;justify-content:center;font-size:32px;font-weight:400}
.f-addr{position:absolute;top:170px;width:1200px;display:flex;justify-content:center;gap:16px;align-items:center;font-size:15px}
.social{position:absolute;top:273px;left:0;width:1200px;height:80px;border-top:1px solid #333;border-bottom:1px solid #333}
.social div{position:absolute;top:0;height:80px;display:flex;align-items:center;justify-content:center;gap:10px;font-size:15px;border-left:1px solid #333}
.sq{width:20px;height:20px;background:#fff;border-radius:3px}
.f-links{position:absolute;top:422px;width:1200px;text-align:center;font-size:15px;word-spacing:4px}
.copy{position:absolute;top:470px;width:1200px;text-align:center;font-size:15px}
</style>
</head>
<body>
<div class="page">

  <!-- header -->
  <div class="abs logo" style="left:100px;top:35px"><span class="logo-mark"></span>CareLoomKits</div>
  <nav class="abs nav">
    <span class="active">Home</span><span>About Us</span><span>Testimonials</span><span>Medical Advisory Board</span>
  </nav>
  <div class="abs btn nav-cta">Contact</div>

  <!-- hero -->
  <div class="abs hero-deco"></div>
  <div class="abs hero-photo" role="img" aria-label="Patient on a sofa holding a tablet showing the CareLoomKits app"></div>
  <div class="abs eyebrow">Digitally Delivering</div>
  <h1 class="abs hero-title">Procedure<br>eCare</h1>
  <div class="abs hero-sub">For 100+ procedures<br>Quickly and economically</div>
  <div class="abs btn hero-cta">Contact Us</div>
  <div class="dot" style="left:234px;top:525px;width:38px;height:38px"></div>
  <div class="dot" style="left:483px;top:627px;width:64px;height:64px"></div>
  <div class="dot" style="left:377px;top:552px;width:7px;height:7px"></div>
  <div class="dot" style="left:330px;top:600px;width:7px;height:7px"></div>
  <div class="dot" style="left:240px;top:695px;width:6px;height:6px"></div>
  <div class="dot" style="left:391px;top:688px;width:6px;height:6px"></div>
  <div class="dot" style="left:440px;top:746px;width:10px;height:10px"></div>

  <!-- intro -->
  <h2 class="abs intro">We enable clinicians to increase the number<br>of procedures - while improving health outcomes</h2>

  <div class="card" style="left:99px">
    <svg width="70" height="74" viewBox="0 0 70 74" fill="none" stroke="#0a7ce6" stroke-width="2.4" aria-hidden="true">
      <rect x="26" y="3" width="40" height="52" rx="5"/><path d="M34 16h24M34 26h24M34 36h16"/>
      <circle cx="18" cy="52" r="14"/><path d="M8 62l20-20"/>
    </svg>
    <h3>Periop Tasks</h3>
    <p>Lorem Ipsum is simply dummy text of the printing and typesetting industry. Lorem Ipsum has been the industry's standard dummy text ever since the 1500s.</p>
  </div>
  <div class="card featured" style="left:446px">
    <svg width="72" height="72" viewBox="0 0 72 72" fill="none" stroke="#fff" stroke-width="2.6" aria-hidden="true">
      <path d="M24 4h24v20h20v24H48v20H24V48H4V24h20z"/><path d="M36 56V34"/>
    </svg>
    <h3>Interactive<br>Symptom Triage</h3>
    <p>Lorem Ipsum is simply dummy text of the printing and typesetting industry. Lorem Ipsum has been the industry's standard dummy text ever since the 1500s,</p>
  </div>
  <div class="card" style="left:794px">
    <svg width="72" height="64" viewBox="0 0 72 64" fill="none" stroke="#0a7ce6" stroke-width="2.4" aria-hidden="true">
      <path d="M34 56L10 32C2 24 4 8 16 6c8-1 14 4 18 10 4-6 10-11 18-10 6 1 10 5 11 10"/>
      <circle cx="52" cy="42" r="14"/><path d="M52 34v16M44 42h16"/>
    </svg>
    <h3>Periop Tasks</h3>
    <p>Lorem Ipsum is simply dummy text of the printing and typesetting industry. Lorem Ipsum has been the industry's standard dummy text ever since the 1500s.</p>
  </div>

  <!-- benefits -->
  <section class="abs benefits">
    <h2 class="sec-title">We have the best ecare<br>solution for surgeries and treatments</h2>
  </section>
  <div class="abs circle-photo" role="img" aria-label="Surgeon and nurse consulting with a patient in a clinic"></div>
  <div class="abs sm-photo" style="left:428px;top:1852px;width:108px;height:108px;background:linear-gradient(135deg,#f0f3f6,#b9c6d3)" role="img" aria-label="Clinician wearing a face mask"></div>
  <div class="abs sm-photo" style="left:343px;top:1955px;width:190px;height:190px" role="img" aria-label="Blood pressure being measured on a patient's arm"></div>

  <div class="abs acc" style="top:1742px;height:168px">
    <h4>Immedite and Measurable Benefits<span style="width:20px;height:3px;background:var(--orange);display:block"></span></h4>
    <p>Lorem Ipsum is simply dummy text of the printing and typesetting industry. Lorem Ipsum has been the industry's standard dummy text ever since the 1500s. Dummy text of the printing and typesetting industry. Lorem Ipsum has been the industry's standard dummy text ever since the 1500s.</p>
  </div>
  <div class="abs acc" style="top:1918px;height:64px"><h4>Improvment in the Entire Patient Journey<span>+</span></h4></div>
  <div class="abs acc" style="top:2007px;height:64px"><h4>Provide Specific<span>+</span></h4></div>
  <div class="abs acc" style="top:2097px;height:66px"><h4>Accessible From Any Device<span>+</span></h4></div>
  <div class="abs acc" style="top:2188px;height:60px;border:0"><h4>No use Manual Needed<span>+</span></h4></div>

  <!-- testimonials -->
  <section class="abs testi-bg"></section>
  <section class="abs testi">
    <div class="bar"></div>
    <h2 class="sec-title">Testimonials</h2>
  </section>
  <div class="abs quote" style="left:503px;top:2518px">&#8220;</div>
  <div class="abs quote" style="left:892px;top:2684px">&#8221;</div>
  <div class="abs" style="left:300px;top:2590px;width:100px;height:100px;border-radius:50%;background:var(--blue)"></div>
  <div class="abs" style="left:323px;top:2608px;width:164px;height:164px;border-radius:50%;background:var(--blue)"></div>
  <div class="abs" style="left:333px;top:2618px;width:144px;height:144px;border-radius:50%;background:#fff"></div>
  <div class="abs" style="left:339px;top:2624px;width:132px;height:132px;border-radius:50%;background:linear-gradient(160deg,#e8e4df,#c9a88e 55%,#5a6b80)" role="img" aria-label="Portrait of Dr. Rowan E. Halden"></div>
  <p class="abs testi-text">The CareLoomKits Peri-op eCare app provides patients with critical information about their diagnosis and treatment. This service guides patients through what is often a very stressful experience, answering common questions that arise during the course of treatment. It's a fantastic support tool for both doctors and patients.</p>
  <div class="abs name">Rowan E. Halden, MD</div>
  <div class="abs role">Associate Professor, Orthopaedic Surgery<br>Calloway Medical School<br>Ashgrove General Hospital</div>
  <div class="abs arrow" style="left:218px;top:2610px;background:#e6e8ec">
    <svg width="14" height="14" viewBox="0 0 14 14" fill="none" stroke="#fff" stroke-width="2"><path d="M9 2L4 7l5 5"/></svg>
  </div>
  <div class="abs arrow" style="left:937px;top:2610px;background:var(--orange)">
    <svg width="14" height="14" viewBox="0 0 14 14" fill="none" stroke="#fff" stroke-width="2"><path d="M5 2l5 5-5 5"/></svg>
  </div>
  <div class="abs pager"><i></i><i></i><i class="on"></i><i></i><i></i></div>

  <!-- clinical groups -->
  <section class="abs groups">
    <h2 class="sec-title">Clinical Groups</h2>
  </section>

  <div class="group" style="left:153px;top:3182px"><span class="g-icon"></span><span class="g-num">01.</span>
    <div class="g-body"><h5>Bariatric</h5><p><b>Talia M. Brenner, MD MS FACS</b><br>Professor of Surgery<br>Calloway Medical School</p></div></div>
  <div class="group" style="left:465px;top:3182px"><span class="g-icon"></span><span class="g-num">02.</span>
    <div class="g-body"><h5>Cardiac Surgery</h5><p><b>Talia M. Brenner, MD MS FACS</b><br>Professor of Surgery<br>Calloway Medical School</p></div></div>
  <div class="group" style="left:776px;top:3182px"><span class="g-icon"></span><span class="g-num">03.</span>
    <div class="g-body"><h5>Fertility Medicine</h5><p><b>Talia M. Brenner, MD MS FACS</b><br>Professor of Surgery<br>Calloway Medical School</p></div></div>
  <div class="group" style="left:153px;top:3328px"><span class="g-icon"></span><span class="g-num">04.</span>
    <div class="g-body"><h5>Gynecology</h5><p><b>Talia M. Brenner, MD MS FACS</b><br>Professor of Surgery<br>Calloway Medical School</p></div></div>
  <div class="group" style="left:465px;top:3328px"><span class="g-icon"></span><span class="g-num">05.</span>
    <div class="g-body"><h5>Lorem Ipsum</h5><p><b>Talia M. Brenner, MD MS FACS</b><br>Professor of Surgery<br>Calloway Medical School</p></div></div>
  <div class="group" style="left:776px;top:3328px"><span class="g-icon"></span><span class="g-num">06.</span>
    <div class="g-body"><h5>Lorem Ipsum</h5><p><b>Talia M. Brenner, MD MS FACS</b><br>Professor of Surgery<br>Calloway Medical School</p></div></div>

  <!-- newsletter -->
  <section class="abs news">
    <h2>Subscribe to Newsletter</h2>
    <p>It is a long established fact that a reader will be distracted by the readable</p>
    <div class="field"><span>Enter you email address</span><span class="btn send">Send Now</span></div>
  </section>

  <!-- footer -->
  <footer class="abs footer">
    <div class="logo f-logo" style="color:#2b8fd6"><span class="logo-mark" style="width:52px;height:52px;background:#2b8fd6"></span>CareLoomKits</div>
    <div class="f-addr">
      <svg width="16" height="20" viewBox="0 0 16 20" aria-hidden="true"><path d="M8 0a8 8 0 0 0-8 8c0 6 8 12 8 12s8-6 8-12a8 8 0 0 0-8-8zm0 11a3 3 0 1 1 0-6 3 3 0 0 1 0 6z" fill="#fff"/></svg>
      <span>CareLoomKits Inc, Boston, USA</span><span>&#8226;</span>
      <svg width="18" height="18" viewBox="0 0 24 24" aria-hidden="true"><path d="M6.6 10.8a15 15 0 0 0 6.6 6.6l2.2-2.2a1 1 0 0 1 1-.25 11 11 0 0 0 3.6.6 1 1 0 0 1 1 1V20a1 1 0 0 1-1 1A17 17 0 0 1 3 4a1 1 0 0 1 1-1h3.5a1 1 0 0 1 1 1c0 1.25.2 2.45.6 3.6a1 1 0 0 1-.25 1z" fill="#fff"/></svg>
      <span>555-014-2290</span>
    </div>
    <div class="social">
      <div style="left:99px;width:333px"><span class="sq"></span>@CareLoomKits</div>
      <div style="left:432px;width:340px"><span class="sq"></span>CareLoomKits on Linkora</div>
      <div style="left:772px;width:329px;border-right:1px solid #333"><span class="sq"></span>Streamly Channel</div>
    </div>
    <div class="f-links">Privacy Policy &nbsp; | &nbsp; Terms of Use &nbsp; | &nbsp; Login</div>
    <div class="copy">©2021 CareLoomKits Inc., CareLoomKits™ and CareLoomKits Inc™ are trademarks of CareLoomKits Inc.</div>
  </footer>
</div>
</body>
</html>
```